business card for mobile ultrasound business
Coastline Portable Scans
business card for mobile ultrasound business - Medical
Creative Brief
Professional
Theodore R. Dalby
Senior Executive
738 Heron Bluff Lane Myrtle Beach, SC 29461
coastlineportablescans@mailbox-example.net

```html
<!DOCTYPE html>
<html lang="en">
<head>
<meta charset="utf-8">
<title>Coastline Portable Scans – Business Card</title>
<link href="https://fonts.googleapis.com/css2?family=Montserrat:wght@400;600&display=swap" rel="stylesheet">
<style>
  :root {
    --page-bg: #e4e4e6;
    --card-white: #ffffff;
    --card-dark: #0d0f12;
    --card-dark-2: #1c2026;
    --brand-blue: #1d8fd6;
    --brand-blue-deep: #0b5f9e;
    --ink: #3a3f45;
    --ink-soft: #7b828a;
    --on-dark: #e9eef3;
    --on-dark-soft: #8d98a4;
  }
  * { box-sizing: border-box; margin: 0; padding: 0; }
  html, body { width: 1200px; height: 982px; overflow: hidden; }
  body {
    background: var(--page-bg);
    font-family: "Montserrat", Arial, sans-serif;
    display: flex;
    align-items: center;
    justify-content: center;
    gap: 60px;
  }
  .card {
    position: relative;
    width: 520px;
    height: 297px;
    border-radius: 16px;
    overflow: hidden;
    box-shadow: 0 10px 30px rgba(0,0,0,0.18);
  }
  .card-edge {
    position: absolute;
    left: 0; top: 0; bottom: 0;
    width: 22px;
    background: linear-gradient(180deg, var(--brand-blue) 0%, var(--brand-blue-deep) 100%);
  }
  /* back */
  .card--back {
    background: radial-gradient(ellipse at 70% 30%, var(--card-dark-2) 0%, var(--card-dark) 70%);
    color: var(--on-dark);
  }
  .card--back .brand {
    position: absolute;
    top: 70px; left: 22px; right: 0;
    text-align: center;
  }
  .card--back .person { position: absolute; left: 48px; bottom: 46px; }
  .card--back .person-name { color: var(--brand-blue); }
  .card--back .person-title { color: var(--on-dark-soft); }
  /* front */
  .card--front { background: var(--card-white); color: var(--ink); }
  .card--front .brand {
    position: absolute;
    top: 46px; right: 40px;
    text-align: right;
  }
  .brand-row { display: inline-flex; align-items: center; gap: 10px; }
  .brand-dot {
    width: 14px; height: 14px; border-radius: 50%;
    background: var(--brand-blue);
  }
  .brand-name {
    font-weight: 600;
    font-size: 19px;
    letter-spacing: 0.06em;
    text-transform: uppercase;
    color: var(--brand-blue);
  }
  .contact {
    position: absolute;
    top: 112px; right: 40px;
    text-align: right;
    font-size: 11px;
    line-height: 1.65;
    color: var(--ink-soft);
  }
  .email {
    position: absolute;
    left: 48px; top: 172px;
    font-size: 10.5px;
    color: var(--ink-soft);
  }
  .card--front .person { position: absolute; left: 48px; bottom: 46px; }
  .person-name {
    font-weight: 600;
    font-size: 17px;
    color: var(--brand-blue);
    letter-spacing: 0.02em;
  }
  .person-title {
    font-size: 11px;
    color: var(--ink-soft);
    margin-top: 3px;
  }
</style>
</head>
<body>
  <section class="card card--back" aria-label="Card back">
    <div class="card-edge"></div>
    <div class="brand">
      <div class="brand-row">
        <span class="brand-dot"></span>
        <span class="brand-name">Coastline Portable Scans</span>
      </div>
    </div>
    <div class="person">
      <p class="person-name">Theodore R. Dalby</p>
      <p class="person-title">Senior Executive</p>
    </div>
  </section>

  <section class="card card--front" aria-label="Card front">
    <div class="card-edge"></div>
    <div class="brand">
      <div class="brand-row">
        <span class="brand-dot"></span>
        <span class="brand-name">Coastline Portable Scans</span>
      </div>
    </div>
    <address class="contact" style="font-style:normal">
      738 Heron Bluff Lane<br>
      Myrtle Beach, SC 29461<br>
      843-555-0148
    </address>
    <p class="email">coastlineportablescans@mailbox-example.net</p>
    <div class="person">
      <p class="person-name">Theodore R. Dalby</p>
      <p class="person-title">Senior Executive</p>
    </div>
  </section>
</body>
</html>
```